Poly Bag Packaging Motorcycle Cables - Veronzo Brand

Poly Bag Dimensions: 33cm(H) x 24cm(W)
We would like to design a genuine Poly Bag Packaging for motorcycle cables.
Veronzo, is one of the leading companies for manufacturing Motorcycles, located in Egypt. Our company is offering high-quality products, the best in the local market, with very competitive prices.
We have a limited time to get this project done, So we Highly appreciate receiving your designs ASAP.
Target Market(s)
Motorcycle Spare parts Buyers
Font styles to use
Colors
Designer to choose colors to be used in the design.
Look and feel
Each slider illustrates characteristics of the customer's brand and the style your logo design should communicate.

```html
<!DOCTYPE html>
<html lang="en">
<head>
<meta charset="UTF-8">
<title>Veronzo Motorcycle Cable Poly Bag</title>
<link href="https://fonts.googleapis.com/css2?family=Montserrat:wght@500;600;800&display=swap" rel="stylesheet">
<style>
  :root {
    --page: #ffffff;
    --film: #f1f1f1;
    --film-edge: #e2e2e2;
    --yellow: #e3dc2a;
    --yellow-light: #f3ee7a;
    --ink: #1a1a1a;
    --window-light: #f4f4f4;
    --window-mid: #e6e6e8;
  }
  * { margin: 0; padding: 0; box-sizing: border-box; }
  html, body {
    width: 1200px; height: 1200px; overflow: hidden;
    background: var(--page);
    font-family: "Montserrat", sans-serif;
  }
  .bag {
    position: absolute;
    left: 320px; top: 106px;
    width: 570px; height: 1012px;
    background: var(--film);
    border: 1px solid var(--film-edge);
    border-radius: 6px 6px 22px 22px;
    overflow: hidden;
  }
  .bag__seal {
    position: absolute; left: 0; top: 0; width: 100%; height: 62px;
    background: repeating-linear-gradient(180deg, #f7f7f7 0 4px, #ececec 4px 6px);
  }
  .label-main {
    position: absolute; left: 0; top: 83px; width: 100%; height: 516px;
    background: linear-gradient(180deg, var(--yellow) 0%, var(--yellow-light) 40%, var(--yellow) 100%);
  }
  .brand {
    position: absolute; left: 0; top: 196px; width: 100%;
    display: flex; align-items: center; justify-content: center; gap: 16px;
  }
  .brand__dot {
    width: 38px; height: 38px; border-radius: 50%;
    background: var(--ink);
  }
  .brand__name {
    font-weight: 800; font-size: 62px; letter-spacing: 3px;
    color: var(--ink); text-transform: uppercase;
  }
  .label-main__copy {
    position: absolute; left: 33px; right: 18px; top: 438px;
    font-size: 11.3px; font-weight: 600; line-height: 14px;
    color: var(--ink);
    hyphens: auto;
  }
  .window {
    position: absolute; left: 0; top: 599px; width: 100%; height: 254px;
    background: linear-gradient(160deg, var(--window-light) 0%, var(--window-mid) 55%, var(--window-light) 100%);
  }
  .label-foot {
    position: absolute; left: 6px; right: 14px; top: 853px; height: 57px;
    background: var(--yellow);
    padding: 12px 10px 0 29px;
  }
  .label-foot__copy {
    font-size: 11.3px; font-weight: 600; line-height: 14px;
    color: var(--ink);
    text-align: justify; text-align-last: justify;
  }
</style>
</head>
<body>
  <div class="bag">
    <div class="bag__seal"></div>

    <div class="label-main">
      <div class="brand">
        <span class="brand__dot"></span>
        <span class="brand__name">Veronzo</span>
      </div>
      <p class="label-main__copy" lang="en">Lorem ipsum dolor sit amet, consectetur adipiscing elit, sed do eiusmod tempor incididunt ut labore et dolore magna aliqua. Quis ipsum suspendisse ultrices gravida. Risus commodo viverra maecenas accumsan lacus vel facilisis.</p>
    </div>

    <div class="window" role="img" aria-label="Clear window showing a coiled black motorcycle cable inside the bag"></div>

    <div class="label-foot">
      <p class="label-foot__copy">Lorem ipsum dolor sit amet, consectetur adipiscing elit, sed do eiusmod tempor incididunt ut labore et dolore magna aliqua. Quis ipsum suspendisse ultrices</p>
    </div>
  </div>
</body>
</html>
```